REDESIGN MAIN BANNER IMAGE FOR MARKETING WEBSITE

I feel like my main banner image is too busy but I like it but i want to see other options. www.brightlanepromoworks.biz I want a nice professional clean design that goes with current theme of site. Must look professional and show the variety of incentives we offer but not be overwelming.

My business is called Brightlane Promo Works and I provide businesses around the world with marketing incentives that they can use to create exciting promotions and contest and marketing giveaways to help attract more customers.

I provide a variety of different types of incentives such as Vacation Certificates, Dining Vouchers, Hotel Savings Cards, Smart Watches, Etc. that businesses can use in their marketing efforts.

I want my main banner image to reflect the variety of different categories of incentives... that I offer here: https://www.brightlanepromoworks.biz/incentives

We can use images of certificates or images.....I just want the content to be the same:

CONTENT FOR MAIN BANNER IMAGE:
INCREASE LEADS AND SALES OVERNIGHT

CREATE EXCITING MARKETING PROMOTIONS GIVING AWAY SMART DEVICES, VACATION CERTIFICATES, DINING VOUCHERS AND OTHER INCENTIVES TO YOUR CUSTOMERS

GET A FREE SAMPLE PACKAGE FOR A LIMITED TIME ONLY

Target Market(s)

b2b business owners, ceo, president, owner, founder

Industry/Entity Type

Promotional

Requirements
Must have
• Hi guys keep in mind the finished product will have to be 1800x840

Nice to have
• I want a nice professional clean design that goes with current theme of site. Must look professional and show the variety of incentives we offer but not be overwelming.
Should not have

```html
<!DOCTYPE html>
<html lang="en">
<head>
<meta charset="utf-8">
<title>Brightlane Promo Works — Main Banner</title>
<link rel="stylesheet" href="https://fonts.googleapis.com/css2?family=Anton&family=Dosis:wght@500;700&family=Montserrat:wght@400;600;800&family=Roboto:wght@500;900&display=swap">
<style>
  :root {
    --promo-orange: #ff5a00;
    --navy: #0f1f40;
    --headline-red: #ee1c25;
    --body-blue: #1b5aa6;
    --deep-blue: #1d3c78;
    --accent-blue: #0c5ea8;
    --free-green: #3fa535;
    --button-green: #4caf50;
    --soft-blue: #d3e6f7;
    --paper: #f1f1f2;
    --white: #ffffff;
  }
  * { box-sizing: border-box; margin: 0; padding: 0; }
  html, body { width: 1200px; height: 795px; overflow: hidden; background: var(--white); }
  .page { position: relative; width: 1200px; height: 795px; overflow: hidden; }

  /* Promo strip */
  .promo-strip {
    position: absolute; left: 0; top: 0; width: 1200px; height: 70px;
    background: var(--promo-orange); color: var(--white);
  }
  .promo-strip__offer {
    position: absolute; left: 184px; top: 9px;
    font-family: "Dosis", sans-serif; font-weight: 500; font-size: 33px; line-height: 1;
    letter-spacing: 0.2px; white-space: nowrap;
  }
  .promo-strip__offer strong { font-weight: 700; font-size: 38px; }
  .promo-strip__field {
    position: absolute; left: 612px; top: 8px; width: 230px; height: 38px;
    background: var(--white); color: #8b8b8b;
    font-family: "Roboto", sans-serif; font-weight: 500; font-size: 15px;
    padding: 10px 10px 0;
  }
  .promo-strip__button {
    position: absolute; left: 842px; top: 8px; width: 157px; height: 38px;
    background: var(--navy); color: var(--white);
    font-family: "Dosis", sans-serif; font-weight: 700; font-size: 17px;
    text-align: center; line-height: 38px;
  }
  .promo-strip__note {
    position: absolute; left: 638px; top: 52px;
    font-family: "Roboto", sans-serif; font-weight: 900; font-size: 13px; letter-spacing: 0.2px;
  }
  .promo-strip__close { position: absolute; left: 1154px; top: 26px; width: 18px; height: 18px; }

  /* Hero */
  .hero { position: absolute; left: 0; top: 70px; width: 1200px; height: 725px; background: var(--paper); }
  .hero__backdrop { position: absolute; inset: 0; width: 100%; height: 100%; }

  .hero__headline {
    position: absolute; left: 70px; top: 102px;
    font-family: "Anton", sans-serif; font-weight: 400; font-size: 77px; line-height: 90px;
    color: var(--headline-red); letter-spacing: 0.4px; white-space: nowrap;
  }
  .hero__lede {
    position: absolute; left: 72px; top: 296px;
    font-family: "Montserrat", sans-serif; font-weight: 400; font-size: 17.4px; line-height: 35px;
    color: var(--body-blue); letter-spacing: 0.1px; white-space: nowrap;
  }
  .hero__offer {
    position: absolute; left: 70px; top: 402px;
    font-family: "Anton", sans-serif; font-size: 25px; line-height: 1;
    color: var(--deep-blue); white-space: nowrap; letter-spacing: 0.3px;
  }
  .hero__offer .free { color: var(--free-green); font-size: 40px; }
  .hero__offer .limited { color: var(--headline-red); }

  .cta { position: absolute; left: 152px; top: 474px; width: 398px; height: 125px; }
  .cta__shape { position: absolute; inset: 0; width: 100%; height: 100%; }
  .cta__label {
    position: absolute; left: 0; top: 16px; width: 100%; text-align: center;
    font-family: "Montserrat", sans-serif; font-weight: 800; font-size: 36px; line-height: 1;
    color: var(--white); letter-spacing: 0.3px;
  }
  .cta__sub {
    position: absolute; left: 0; top: 60px; width: 100%; text-align: center;
    font-family: "Montserrat", sans-serif; font-weight: 400; font-size: 25px; line-height: 1;
    color: var(--soft-blue);
  }

  .incentive-collage { position: absolute; left: 690px; top: 78px; width: 460px; height: 540px; }
</style>
</head>
<body>
<div class="page">

  <header class="promo-strip">
    <p class="promo-strip__offer">Get <strong>65%</strong> OFF Your First Month</p>
    <div class="promo-strip__field">Mobile Number</div>
    <div class="promo-strip__button">Get My Discount</div>
    <p class="promo-strip__note">NEW CUSTOMERS ONLY - LIMITED TIME ONLY!</p>
    <svg class="promo-strip__close" viewBox="0 0 18 18" aria-label="Close">
      <circle cx="9" cy="9" r="9" fill="#f2b8a0"/>
      <path d="M5.5 5.5 L12.5 12.5 M12.5 5.5 L5.5 12.5" stroke="#ffffff" stroke-width="2" stroke-linecap="round"/>
    </svg>
  </header>

  <section class="hero">
    <svg class="hero__backdrop" viewBox="0 0 2094 1026" preserveAspectRatio="none" aria-hidden="true">
      <defs>
        <linearGradient id="paperShade" x1="0" y1="0" x2="1" y2="1">
          <stop offset="0" stop-color="#ebebec"/>
          <stop offset="1" stop-color="#f6f6f7"/>
        </linearGradient>
      </defs>
      <rect width="2094" height="1026" fill="url(#paperShade)"/>
      <polygon points="175,0 520,0 120,1026 0,1026 0,265" fill="#f7f7f8"/>
      <polygon points="900,0 1000,0 520,1026 380,1026" fill="#f8f8f9"/>
      <polygon points="1340,0 1560,0 1260,1026 1000,1026" fill="#f9f9fa"/>
      <polygon points="1600,0 2094,0 2094,195 1800,1026 1200,1026" fill="#fbfbfc"/>
      <polygon points="0,0 175,0 0,265" fill="var(--accent-blue)"/>
      <polygon points="2094,195 2094,1026 1800,1026" fill="var(--accent-blue)"/>
    </svg>

    <h1 class="hero__headline">INCREASE LEADS AND<br>SALES OVERNIGHT</h1>

    <p class="hero__lede">CREATE EXCITING MARKETING PROMOTIONS GIVING AWAY<br>SMART DEVICES, VACATION CERTIFICATES, DINING VOUCHERS<br>AND OTHER INCENTIVES TO YOUR CUSTOMERS</p>

    <p class="hero__offer">GET A <span class="free">FREE</span> SAMPLE PACKAGE FOR A <span class="limited">LIMITED TIME</span> ONLY</p>

    <div class="cta">
      <svg class="cta__shape" viewBox="0 0 400 125" preserveAspectRatio="none" aria-hidden="true">
        <defs>
          <radialGradient id="ctaShadow" cx="0.5" cy="0.5" r="0.5">
            <stop offset="0" stop-color="#000" stop-opacity="0.28"/>
            <stop offset="1" stop-color="#000" stop-opacity="0"/>
          </radialGradient>
        </defs>
        <ellipse cx="200" cy="112" rx="200" ry="12" fill="url(#ctaShadow)"/>
        <path d="M2 6 Q2 0 10 0 L390 0 Q399 0 398 8 L394 80 Q393 88 385 89 L205 95 L12 88 Q5 87 5 80 Z" fill="var(--button-green)"/>
      </svg>
      <p class="cta__label">GET FREE SAMPLE</p>
      <p class="cta__sub">100% FREE</p>
    </div>

    <svg class="incentive-collage" viewBox="0 0 460 540" role="img" aria-label="Circular collage of printed incentive certificates: hotel stays, airfare, dining, cruise and resort vouchers">
      <defs>
        <radialGradient id="collageTone" cx="0.5" cy="0.5" r="0.5">
          <stop offset="0" stop-color="#f3f3f5"/>
          <stop offset="0.5" stop-color="#ece6e7"/>
          <stop offset="0.85" stop-color="#d9a2a6"/>
          <stop offset="1" stop-color="#c44a52"/>
        </radialGradient>
      </defs>
      <ellipse cx="230" cy="270" rx="225" ry="265" fill="url(#collageTone)"/>
    </svg>
  </section>

</div>
</body>
</html>
```